Furniture Wholesaler PowerPoint Template Refresh

Harlow Goods is a family owned and operated furniture wholesaler that works with retailers like Dunmoor, Pellix, and Brimshelf to sell multifunctional furniture and home décor pieces.

We are looking for a new company PowerPoint template, primarily to be used by our sales team when working with our new and existing retail partners. Our current slideshow deck is attached below. We would like the new design to have a more modern and minimalist feel with at least 3-4 slide design options.

Our current logo is also included in the old slideshow attached below, but we are not looking to emphasize it in the new PowerPoint design.

Target Market(s)

This presentation will be used by our sales team to inform existing and potential retail partners of our company history, product selections, and fulfillment capabilities.

Industry/Entity Type

Ecommerce

Font styles to use
Other font styles liked:
• Please use Windows system fonts for any text. Our logo font is Myriad Pro, which should only be used for any graphics.

Colors

Designer to choose colors to be used in the design.

Requirements
Must have
• - at least 3-4 slide design options
- redesign of the image on slide 4 in the old presentation (attached below)
- same slide layout options as the old presentation, including a cover slide, title with text slide, title with text and image slide, and title with image slide.
- Blue and white as main colors with red as the accent. RGB codes are:
Blue - R0, G67, B104
White - R255, G255, B255
Red - R181, G36, B25
Should not have
• - do not emphasize our logo in new design (especially the blue ball)

```html
<!DOCTYPE html>
<html lang="en">
<head>
<meta charset="utf-8">
<title>Harlow Goods – Fulfillment Slide</title>
<link rel="stylesheet" href="https://fonts.googleapis.com/css2?family=Open+Sans:wght@400;600;700;800&display=swap">
<style>
  :root {
    --blue: #004368;
    --red: #b52419;
    --white: #ffffff;
    --page: #ffffff;
    --map-light: #e4e6e9;
    --map-mid: #c9ccd1;
    --track: #e6e8eb;
    --ink-soft: #5a6470;
  }
  * { box-sizing: border-box; margin: 0; padding: 0; }
  html, body { width: 900px; height: 1200px; overflow: hidden; background: var(--page); }
  body { font-family: "Open Sans", Arial, sans-serif; position: relative; }

  .slide {
    position: absolute; left: 24px; top: 325px;
    width: 852px; height: 520px;
    background: var(--white);
    box-shadow: 0 2px 10px rgba(0,0,0,.12);
    overflow: hidden;
  }
  .slide-title {
    position: absolute; left: 36px; top: 42px;
    font-size: 34px; font-weight: 800; color: var(--blue); letter-spacing: -0.5px;
  }
  .slide-title .accent { color: var(--red); }

  .side-band {
    position: absolute; right: 0; top: 0; width: 46px; height: 100%;
    background: var(--blue);
  }
  .side-band .page-number {
    position: absolute; top: 46px; width: 100%; text-align: center;
    color: var(--white); font-size: 11px; font-weight: 600;
  }
  .side-band .section-label {
    position: absolute; top: 210px; left: 50%;
    transform: translate(-50%, 0) rotate(90deg);
    white-space: nowrap; color: var(--white); font-size: 9px; opacity: .85; letter-spacing: .5px;
  }
  .side-band .corner-mark {
    position: absolute; bottom: 18px; left: 50%; transform: translateX(-50%);
    width: 22px; height: 22px; border: 2px solid var(--white);
  }

  .map-area {
    position: absolute; left: 150px; top: 110px; width: 580px; height: 240px;
    background: radial-gradient(ellipse at 50% 45%, var(--map-mid), var(--map-light) 70%);
    border-radius: 40px 70px 30px 90px;
  }

  .hub-label {
    position: absolute; left: 370px; top: 210px; width: 150px;
    display: flex; align-items: center; justify-content: center; gap: 8px;
    color: var(--blue); font-weight: 800; font-size: 16px; white-space: nowrap;
  }
  .hub-label .hub-square { width: 12px; height: 12px; background: var(--blue); }

  .pin { position: absolute; width: 26px; height: 34px; }
  .pin-label {
    position: absolute; font-size: 7px; color: var(--ink-soft); white-space: nowrap;
  }

  .stamp-same-day {
    position: absolute; left: 50px; top: 122px; width: 104px; height: 56px;
    border: 3px solid var(--red); color: var(--red); border-radius: 6px;
    transform: rotate(-18deg); text-align: center; padding-top: 5px;
  }
  .stamp-same-day .big { font-size: 17px; font-weight: 800; line-height: 1.1; }
  .stamp-same-day .small { font-size: 13px; font-weight: 700; }

  .stamp-delivery {
    position: absolute; left: 686px; top: 230px; width: 104px; height: 104px;
    border: 3px solid var(--red); border-radius: 50%; color: var(--red);
    display: flex; align-items: center; justify-content: center; text-align: center;
    transform: rotate(-22deg); font-weight: 800; font-size: 12px; line-height: 1.15;
    background: var(--white);
  }
  .stamp-delivery::before {
    content: ""; position: absolute; inset: 5px; border: 1.5px solid var(--red); border-radius: 50%;
  }

  .delivery-stats { position: absolute; left: 36px; top: 378px; display: flex; gap: 26px; }
  .stat { width: 80px; text-align: center; }
  .stat svg { display: block; margin: 0 auto 6px; }
  .stat-label { font-size: 8px; color: var(--ink-soft); font-weight: 600; white-space: nowrap; }

  .messaging { position: absolute; left: 470px; top: 368px; }
  .messaging-title { color: var(--red); font-size: 20px; font-weight: 700; line-height: 1.05; }
  .messaging-note { margin-top: 8px; display: flex; align-items: center; gap: 6px; font-size: 10px; color: var(--blue); font-weight: 600; }
</style>
</head>
<body>
  <section class="slide">
    <h1 class="slide-title">We are <span class="accent">Fulfillment Experts</span></h1>

    <div class="map-area" role="img" aria-label="Map of the United States with warehouse locations highlighted"></div>

    <div class="hub-label"><span class="hub-square"></span>Harlow Goods</div>

    <svg class="pin" style="left:218px;top:188px" viewBox="0 0 26 34" aria-hidden="true">
      <path d="M13 33C13 33 2 19 2 12a11 11 0 0 1 22 0c0 7-11 21-11 21z" fill="var(--blue)"/>
      <circle cx="13" cy="12" r="4" fill="var(--red)"/>
    </svg>
    <span class="pin-label" style="left:244px;top:210px">Reno, NV</span>

    <svg class="pin" style="left:418px;top:300px" viewBox="0 0 26 34" aria-hidden="true">
      <path d="M13 33C13 33 2 19 2 12a11 11 0 0 1 22 0c0 7-11 21-11 21z" fill="var(--blue)"/>
      <circle cx="13" cy="12" r="4" fill="var(--red)"/>
    </svg>
    <span class="pin-label" style="left:444px;top:322px">Dallas, TX</span>

    <svg class="pin" style="left:628px;top:166px" viewBox="0 0 26 34" aria-hidden="true">
      <path d="M13 33C13 33 2 19 2 12a11 11 0 0 1 22 0c0 7-11 21-11 21z" fill="var(--blue)"/>
      <circle cx="13" cy="12" r="4" fill="var(--red)"/>
    </svg>
    <span class="pin-label" style="left:654px;top:188px">Allentown, PA</span>

    <div class="stamp-same-day">
      <div class="big">SAME DAY</div>
      <div class="small">Shipping</div>
    </div>

    <div class="stamp-delivery">FASTER<br>DELIVERY<br>LOWER COST</div>

    <div class="delivery-stats">
      <div class="stat">
        <svg width="56" height="56" viewBox="0 0 56 56" aria-hidden="true">
          <circle cx="28" cy="28" r="22" fill="none" stroke="var(--track)" stroke-width="7"/>
          <circle cx="28" cy="28" r="22" fill="none" stroke="var(--blue)" stroke-width="7"
                  stroke-dasharray="55.3 138.2" transform="rotate(-90 28 28)"/>
          <text x="28" y="32" text-anchor="middle" font-size="11" font-weight="700" fill="var(--blue)" font-family="Open Sans, sans-serif">40%</text>
        </svg>
        <div class="stat-label">Next Day Delivery</div>
      </div>
      <div class="stat">
        <svg width="56" height="56" viewBox="0 0 56 56" aria-hidden="true">
          <circle cx="28" cy="28" r="22" fill="none" stroke="var(--track)" stroke-width="7"/>
          <circle cx="28" cy="28" r="22" fill="none" stroke="var(--red)" stroke-width="7"
                  stroke-dasharray="117.5 138.2" transform="rotate(-90 28 28)"/>
          <text x="28" y="32" text-anchor="middle" font-size="11" font-weight="700" fill="var(--red)" font-family="Open Sans, sans-serif">85%</text>
        </svg>
        <div class="stat-label">2 Days or less</div>
      </div>
      <div class="stat">
        <svg width="56" height="56" viewBox="0 0 56 56" aria-hidden="true">
          <circle cx="28" cy="28" r="22" fill="none" stroke="var(--blue)" stroke-width="7"/>
          <text x="28" y="32" text-anchor="middle" font-size="11" font-weight="700" fill="var(--blue)" font-family="Open Sans, sans-serif">100%</text>
        </svg>
        <div class="stat-label">3 Days or less</div>
      </div>
    </div>

    <div class="messaging">
      <div class="messaging-title">2 DAY DELIVERY<br>MESSAGING</div>
      <div class="messaging-note">
        <svg width="14" height="12" viewBox="0 0 14 12" aria-hidden="true"><path d="M7 0L14 12H0z" fill="var(--red)"/></svg>
        Increase sale by 25%
      </div>
    </div>

    <aside class="side-band">
      <div class="page-number">3</div>
      <div class="section-label">Harlow Goods | Fulfillment Services</div>
      <div class="corner-mark"></div>
    </aside>
  </section>
</body>
</html>
```